Cat sitting business Web Design Project ***

I have a cat sitting business where I either take care of cats in their home or board them in mine

I need a website which offers my services, my rates, about me, FAQ's, Hours of operation and service areas covered, testimonials, contact info, newsletter sign up, gallery of photos and the ability for me to go in and update when needed.

Coded - Design and coding required

5+ page

```html
<!DOCTYPE html>
<html lang="en">
<head>
<meta charset="utf-8">
<title>Whisker Haven Cat Sitting</title>
<link href="https://fonts.googleapis.com/css2?family=Playfair+Display:ital,wght@0,400;0,700;1,400&family=Open+Sans:ital,wght@0,400;0,600;0,700;1,400&family=Raleway:wght@500;600&display=swap" rel="stylesheet">
<style>
:root{
  --rose:#df9498;
  --rose-deep:#c9686e;
  --salmon:#f8999b;
  --green:#7fbf4d;
  --ink:#222;
  --body:#555;
  --muted:#888;
  --line:#e6e6e6;
  --white:#fff;
}
*{margin:0;padding:0;box-sizing:border-box}
html,body{width:1200px;height:4115px;overflow:hidden}
body{position:relative;background:var(--white);font-family:"Open Sans",sans-serif;color:var(--body)}
.abs{position:absolute}
.center{left:0;width:1200px;text-align:center}

/* top bar */
.topbar{top:0;left:0;width:1200px;height:64px;background:var(--rose);color:var(--white);font-size:12px}
.topbar .info{top:18px;left:80px;display:flex;gap:30px;align-items:center}
.topbar .info span{display:flex;align-items:center;gap:8px}
.topbar .socials{top:20px;right:80px;display:flex;gap:14px}
.dot{width:11px;height:11px;border-radius:50%;background:var(--white);display:block}
.torn{left:0;width:1200px}

/* header */
.brand{display:flex;align-items:center;gap:12px}
.brand .mark{width:74px;height:74px;border-radius:50%;border:2px solid var(--green);display:block}
.brand .name{font-family:"Playfair Display",serif;font-size:22px;line-height:1.1;color:var(--rose-deep)}
.header-brand{top:84px;left:66px}
.nav{top:110px;left:388px;display:flex;gap:0;font-family:"Raleway",sans-serif;font-weight:600;font-size:14.5px;color:var(--ink)}
.nav a{text-decoration:none;color:inherit;position:absolute;white-space:nowrap}
.nav a.active{color:var(--rose-deep)}

/* hero */
.hero{top:170px;left:0;width:1200px;height:672px;background:linear-gradient(100deg,#ebe7e3 0%,#dcd6d0 45%,#bfb4a9 70%,#8f8378 100%)}
.hero h1{top:160px;left:122px;font-family:"Playfair Display",serif;font-weight:700;font-size:50px;line-height:64px;color:#2c2c2c;letter-spacing:1px}
.hero h1 em{font-style:normal;color:var(--rose-deep)}
.btn{display:inline-block;border-radius:30px;font-family:"Raleway",sans-serif;font-weight:600;color:var(--white);background:var(--rose);text-align:center}
.hero .btn{top:386px;left:110px;width:180px;height:54px;line-height:54px;font-size:22px}
.arrow{width:54px;height:54px;border-radius:50%;background:rgba(255,255,255,.35);display:flex;align-items:center;justify-content:center}

/* section heads */
.paw{display:flex;justify-content:center;align-items:center;gap:8px;color:var(--green);font-size:11px;letter-spacing:1px}
.kicker{font-family:"Playfair Display",serif;font-size:13px;color:#444}
.kicker.italic{font-style:italic;color:#777;font-size:12.5px}
.title{font-family:"Playfair Display",serif;font-weight:700;font-size:38px;color:var(--ink);letter-spacing:1px}

/* about */
.ph{display:block}
.about-text{left:620px;width:500px;font-size:12px;line-height:24px}
.ticks{list-style:none;font-size:12px;color:#333;font-weight:600}
.ticks li{display:flex;align-items:center;gap:12px;height:30px}
.ticks li::before{content:"";width:9px;height:9px;border:2px solid var(--rose);border-radius:50%}

/* services */
.service{background:var(--white);border:1px solid var(--line);height:180px;width:510px}
.service h3{position:absolute;top:40px;left:106px;font-family:"Playfair Display",serif;font-weight:700;font-size:15px;color:var(--ink)}
.service p{position:absolute;top:72px;left:106px;width:360px;font-size:12.5px;line-height:24px}
.service .icon{position:absolute;top:26px;left:18px;width:76px;height:90px;border-radius:8px;background:linear-gradient(#eee,#ddd)}

/* testimonial */
.quote{font-family:"Playfair Display",serif;font-style:italic;font-size:16px;line-height:29px;color:#555}

/* appointment */
.appt{top:3050px;left:0;width:1200px;height:745px;background:var(--salmon)}
.field{position:absolute;height:46px;background:var(--white);border-radius:24px;font-size:12px;color:#777;padding:15px 22px}
.appt .title,.appt .kicker{color:var(--white)}

/* footer */
.sub-box{top:3943px;left:470px;width:305px;height:40px;border:1px solid #ddd;border-radius:20px;font-size:12px;color:#777;padding:11px 14px}
.sub-box .btn{position:absolute;top:-1px;right:-1px;width:108px;height:40px;line-height:40px;font-size:13px;font-weight:500}
.foot-social{top:4016px;left:545px;display:flex;gap:16px}
.foot-social .dot{background:#666}
.copyright{top:4075px;font-size:13.5px;color:#555;font-family:"Raleway",sans-serif}
</style>
</head>
<body>

<!-- top bar -->
<div class="abs topbar">
  <div class="abs info">
    <span><svg width="10" height="13" viewBox="0 0 10 13"><path d="M5 0a5 5 0 0 0-5 5c0 4 5 8 5 8s5-4 5-8a5 5 0 0 0-5-5zm0 7a2 2 0 1 1 0-4 2 2 0 0 1 0 4z" fill="#fff"/></svg>18 Maple Row, Fernview FL</span>
    <span><svg width="13" height="13" viewBox="0 0 24 24"><path d="M6.6 10.8a15 15 0 0 0 6.6 6.6l2.2-2.2a1 1 0 0 1 1-.25 11 11 0 0 0 3.6.6 1 1 0 0 1 1 1V20a1 1 0 0 1-1 1A17 17 0 0 1 3 4a1 1 0 0 1 1-1h3.5a1 1 0 0 1 1 1c0 1.25.2 2.45.6 3.6a1 1 0 0 1-.25 1z" fill="#fff"/></svg>+(1) 555 010 2200</span>
    <span><svg width="13" height="10" viewBox="0 0 13 10"><rect width="13" height="10" rx="1" fill="#fff"/><path d="M0 1l6.5 5L13 1" stroke="#df9498" fill="none"/></svg>hello@whiskerhaven.example</span>
  </div>
  <div class="abs socials"><span class="dot"></span><span class="dot"></span><span class="dot"></span><span class="dot"></span><span class="dot"></span></div>
</div>
<svg class="abs torn" style="top:56px" height="16" viewBox="0 0 1200 16" preserveAspectRatio="none"><path d="M0 0H1200V6L1180 10 1150 5 1120 11 1090 6 1060 12 1020 6 990 10 950 5 910 11 870 6 830 10 790 5 750 12 710 6 670 10 630 5 590 11 550 6 510 10 470 5 430 12 390 6 350 10 310 5 270 11 230 6 190 10 150 5 110 11 70 6 30 10 0 5Z" fill="var(--rose)"/></svg>

<!-- header -->
<div class="abs brand header-brand">
  <span class="mark"></span>
  <span class="name">Whisker Haven<br>Cat Sitting</span>
</div>
<nav class="abs nav">
  <a class="active" style="left:0">HOME</a>
  <a style="left:97px">ABOUT</a>
  <a style="left:193px">SERVICES</a>
  <a style="left:321px">COSTS</a>
  <a style="left:418px">FAQ</a>
  <a style="left:514px">TESTIMONIALS</a>
  <a style="left:674px">CONTACT</a>
</nav>

<!-- hero -->
<section class="abs hero" role="img" aria-label="Photo of a fluffy blue-eyed cat held in a person's arms">
  <h1 class="abs">We Feed, Walk and<br>Play with your <em>Loving Cat,</em><br>each visit!</h1>
  <span class="abs btn">CALL NOW!</span>
  <span class="abs arrow" style="top:310px;left:40px"><svg width="10" height="14" viewBox="0 0 10 14"><path d="M8 1L2 7l6 6" stroke="#fff" stroke-width="1.5" fill="none"/></svg></span>
  <span class="abs arrow" style="top:310px;left:1106px"><svg width="10" height="14" viewBox="0 0 10 14"><path d="M2 1l6 6-6 6" stroke="#fff" stroke-width="1.5" fill="none"/></svg></span>
</section>
<svg class="abs torn" style="top:826px" height="18" viewBox="0 0 1200 18" preserveAspectRatio="none"><path d="M0 18H1200V8L1170 12 1140 6 1100 11 1060 5 1020 10 980 6 940 12 900 5 860 10 820 6 780 11 740 5 700 10 660 6 620 12 580 5 540 10 500 6 460 11 420 5 380 10 340 6 300 12 260 5 220 10 180 6 140 11 100 5 60 10 20 6 0 9Z" fill="#fff"/></svg>

<!-- about -->
<div class="abs center paw" style="top:893px">:::::: <svg width="22" height="20" viewBox="0 0 22 20"><ellipse cx="11" cy="14" rx="6" ry="5" fill="var(--green)"/><circle cx="4" cy="8" r="2.6" fill="var(--green)"/><circle cx="8.5" cy="3.5" r="2.6" fill="var(--green)"/><circle cx="13.5" cy="3.5" r="2.6" fill="var(--green)"/><circle cx="18" cy="8" r="2.6" fill="var(--green)"/></svg> ::::::</div>
<div class="abs center kicker" style="top:937px">Welcome to Whisker Haven Cat Sitting</div>
<h2 class="abs center title" style="top:958px">Your Local Professional Cat Sitting Service</h2>
<div class="abs ph" style="top:1042px;left:80px;width:510px;height:403px;background:linear-gradient(135deg,#f1d3d0,#e8c5c2 40%,#4a3c39 60%,#e9e4e0)" role="img" aria-label="Photo of a woman cuddling a white cat in a bedroom"></div>
<div class="abs about-text" style="top:1042px">
  <p>Broadcast neglectful and poignantly well until and some listlessly amidst suc cessful concentrically ably dachshund more far but forwardly echidna outside tiger split thanks far vibrantly gosh hence pangolin however notwithstanding leapt untruthful gauchely yikes komodo dully more.</p>
  <p style="margin-top:18px">As abandoned winced this more far wow jeepers near more wow goodness so revealed much along worm some grasshopper.</p>
</div>
<ul class="abs ticks" style="top:1237px;left:620px">
  <li>Abore et dolore magna aliqua ut enim veniam</li>
  <li>Quis nostrud exercitation ullamco laboris nisi aliquip</li>
  <li>Eiusmod tempor incididunt labore.</li>
</ul>
<span class="abs btn" style="top:1372px;left:620px;width:195px;height:46px;line-height:46px;font-size:16px">READ MORE</span>

<!-- services -->
<div class="abs" style="top:1690px;left:530px;width:670px;height:228px;background:linear-gradient(90deg,#fff 0%,#fff 20%,#f4e4cf 45%,#c9d9ee 70%,#fff 100%);opacity:.7" role="img" aria-label="Photo of colourful cat toys"></div>
<div class="abs center paw" style="top:1572px">:::::: <svg width="22" height="20" viewBox="0 0 22 20"><ellipse cx="11" cy="14" rx="6" ry="5" fill="var(--green)"/><circle cx="4" cy="8" r="2.6" fill="var(--green)"/><circle cx="8.5" cy="3.5" r="2.6" fill="var(--green)"/><circle cx="13.5" cy="3.5" r="2.6" fill="var(--green)"/><circle cx="18" cy="8" r="2.6" fill="var(--green)"/></svg> ::::::</div>
<div class="abs center kicker italic" style="top:1616px">Because We Really Care About Your Pets</div>
<h2 class="abs center title" style="top:1640px">Our Services</h2>
<div class="abs service" style="top:1722px;left:80px">
  <span class="icon" role="img" aria-label="Illustration of a woman walking a cat"></span>
  <h3>Boarding Service</h3>
  <p>Abore et dolore magna aliqua ut enim minim veniam quis nostrud exercitation ullamco laboris nisi aliquip eiusmod tempor incididunt labore.</p>
</div>
<div class="abs service" style="top:1722px;left:612px">
  <span class="icon" role="img" aria-label="Illustration of a sitting cat"></span>
  <h3>Cat Sitting Service</h3>
  <p style="left:106px">Abore et dolore magna aliqua ut enim minim veniam quis nostrud exercitation ullamco laboris nisi aliquip eiusmod tempor incididunt labore.</p>
</div>

<!-- gallery -->
<div class="abs center paw" style="top:2028px">:::::: <svg width="22" height="20" viewBox="0 0 22 20"><ellipse cx="11" cy="14" rx="6" ry="5" fill="var(--green)"/><circle cx="4" cy="8" r="2.6" fill="var(--green)"/><circle cx="8.5" cy="3.5" r="2.6" fill="var(--green)"/><circle cx="13.5" cy="3.5" r="2.6" fill="var(--green)"/><circle cx="18" cy="8" r="2.6" fill="var(--green)"/></svg> ::::::</div>
<div class="abs center kicker" style="top:2072px">A Loving Alternative to Catteries</div>
<h2 class="abs center title" style="top:2094px">From Our Gallery</h2>
<div class="abs ph" style="top:2200px;left:53px;width:260px;height:260px;background:linear-gradient(135deg,#3a2f28,#7a6a5d 50%,#2c241f)" role="img" aria-label="Photo of a tabby cat being petted"></div>
<div class="abs ph" style="top:2200px;left:331px;width:260px;height:260px;background:linear-gradient(135deg,#d9cfc6,#8a7d70 50%,#cfc4b9)" role="img" aria-label="Photo of a green-eyed tabby cat lying on a carpet"></div>
<div class="abs ph" style="top:2200px;left:609px;width:260px;height:260px;background:linear-gradient(135deg,#e89a5a,#f3ebe4 55%,#d8b08a)" role="img" aria-label="Photo of a ginger cat eating from a bowl"></div>
<div class="abs ph" style="top:2200px;left:887px;width:260px;height:260px;background:linear-gradient(135deg,#e9e4e3,#9c8f86 55%,#c9c4c4)" role="img" aria-label="Photo of a sleeping cat being brushed"></div>

<!-- testimonials -->
<div class="abs center paw" style="top:2524px">:::::: <svg width="22" height="20" viewBox="0 0 22 20"><ellipse cx="11" cy="14" rx="6" ry="5" fill="var(--green)"/><circle cx="4" cy="8" r="2.6" fill="var(--green)"/><circle cx="8.5" cy="3.5" r="2.6" fill="var(--green)"/><circle cx="13.5" cy="3.5" r="2.6" fill="var(--green)"/><circle cx="18" cy="8" r="2.6" fill="var(--green)"/></svg> ::::::</div>
<div class="abs center kicker italic" style="top:2568px">Because We Really Care About Your Pets</div>
<h2 class="abs center title" style="top:2587px;font-size:35px">Read Testimonials</h2>
<svg class="abs" style="top:2675px;left:584px" width="33" height="28" viewBox="0 0 33 28"><path d="M0 28V14L8 0h6L9 13h6v15zM18 28V14L26 0h6l-5 13h6v15z" fill="var(--rose)"/></svg>
<p class="abs center quote" style="top:2728px;left:190px;width:820px">And taped a amazingly lazily far gosh oh bald oh raffishly ouch ladybug far that the and alas slapped alas far brusque pridefully kneeled python horse alas sound because more prodigiously outgrew tortoise characteristic stupidly barring therefore so sniffed before drank.</p>
<div class="abs" style="top:2843px;left:569px;width:62px;height:62px;border-radius:50%;background:linear-gradient(135deg,#d9c8bd,#f3efec)" role="img" aria-label="Portrait of the pet owner with her dog"></div>
<div class="abs center" style="top:2923px;font-weight:600;font-size:15px;color:var(--ink)">Nora Bellweather</div>
<div class="abs center" style="top:2950px;font-size:10px;color:#666">PET OWNER</div>

<!-- appointment -->
<svg class="abs torn" style="top:3040px" height="14" viewBox="0 0 1200 14" preserveAspectRatio="none"><path d="M0 14V6L40 9 80 4 120 10 160 5 200 9 240 3 280 10 320 5 360 9 400 4 440 10 480 5 520 9 560 3 600 10 640 5 680 9 720 4 760 10 800 5 840 9 880 3 920 10 960 5 1000 9 1040 4 1080 10 1120 5 1160 9 1200 4V14Z" fill="var(--salmon)"/></svg>
<section class="abs appt">
  <div class="abs center paw" style="top:80px;color:#fff">:::::: <svg width="22" height="20" viewBox="0 0 22 20"><ellipse cx="11" cy="14" rx="6" ry="5" fill="#fff"/><circle cx="4" cy="8" r="2.6" fill="#fff"/><circle cx="8.5" cy="3.5" r="2.6" fill="#fff"/><circle cx="13.5" cy="3.5" r="2.6" fill="#fff"/><circle cx="18" cy="8" r="2.6" fill="#fff"/></svg> ::::::</div>
  <div class="abs center kicker italic" style="top:124px">Because We Really Care About Your Pets</div>
  <h2 class="abs center title" style="top:141px;font-size:35px">Get An Appointment</h2>
  <div class="field" style="top:225px;left:80px;width:333px">Name</div>
  <div class="field" style="top:225px;left:434px;width:333px">Email</div>
  <div class="field" style="top:225px;left:788px;width:333px">Phone #</div>
  <div class="field" style="top:292px;left:80px;width:333px">Date &amp; Time<svg style="position:absolute;right:24px;top:16px" width="12" height="12" viewBox="0 0 12 12"><rect x="0.5" y="1.5" width="11" height="10" fill="none" stroke="#666"/><path d="M0 4h12" stroke="#666"/></svg></div>
  <div class="field" style="top:292px;left:434px;width:333px">Pet Category</div>
  <div class="field" style="top:292px;left:788px;width:333px">Service Type</div>
  <div class="field" style="top:359px;left:80px;width:1041px;height:124px;border-radius:14px">Your Comments...</div>
  <span class="abs btn" style="top:517px;left:512px;width:176px;height:46px;line-height:44px;font-size:14px;font-weight:500;background:#fff;color:#444;border:1px solid #eee">SEND REQUEST</span>
</section>
<svg class="abs torn" style="top:3782px" height="16" viewBox="0 0 1200 16" preserveAspectRatio="none"><path d="M0 0H1200V8L1160 12 1120 6 1080 11 1040 5 1000 10 960 6 920 12 880 5 840 10 800 6 760 11 720 5 680 10 640 6 600 12 560 5 520 10 480 6 440 11 400 5 360 10 320 6 280 12 240 5 200 10 160 6 120 11 80 5 40 10 0 6Z" fill="var(--salmon)"/></svg>

<!-- footer -->
<div class="abs center" style="top:3828px;display:flex;flex-direction:column;align-items:center;gap:8px">
  <span style="width:70px;height:70px;border-radius:50%;border:2px solid var(--green);display:block"></span>
  <span style="font-family:'Playfair Display',serif;font-size:21px;line-height:1.1;color:var(--rose-deep)">Whisker Haven<br>Cat Sitting</span>
</div>
<div class="abs sub-box">Enter your email<span class="btn">SUBSCRIBE</span></div>
<div class="abs foot-social"><span class="dot"></span><span class="dot"></span><span class="dot"></span><span class="dot"></span><span class="dot"></span></div>
<div class="abs" style="top:4056px;left:57px;width:1086px;height:1px;background:var(--line)"></div>
<div class="abs center copyright">Copyright 2022 Whisker Haven Cat Sitting. All rights reserved.</div>

</body>
</html>
```